Poster design needed for Pregnant class 25.11.2018*

We need a poster design with the instruction details:
- Size: A4- Content:
1. Logo
2. Title of poster: Pregnant class - Eating healthy while pregnant
3. Promote when join in out class: 30% off delivery package
4. Singapore - 25.11.2018
5. Detail of contact: please visit https://www.harbourvalehospital.com.sg/And get information for this poster.

Pregnant

Medical And Science

Sans Serif

85cae6
33a6d7

• Picture mom and baby or pregnant

```html
<!DOCTYPE html>
<html lang="en">
<head>
<meta charset="utf-8">
<title>Pregnant Class Poster</title>
<link href="https://fonts.googleapis.com/css2?family=Montserrat:ital,wght@0,400;0,500;0,600;0,700;1,600&display=swap" rel="stylesheet">
<style>
  :root {
    --stage: #e6e6e4;
    --blue: #2b57a6;
    --teal: #19b3a6;
    --olive: #a59d76;
    --orange: #ef5a2a;
    --ink: #1f1f24;
    --navy: #2b2872;
    --white: #ffffff;
  }
  * { margin: 0; padding: 0; box-sizing: border-box; }
  html, body { width: 1200px; height: 1200px; overflow: hidden; }
  body {
    background: var(--stage);
    font-family: "Montserrat", sans-serif;
    color: var(--ink);
    position: relative;
  }
  .poster {
    position: absolute;
    left: 222px; top: 40px;
    width: 778px; height: 1100px;
    overflow: hidden;
    background: #f6f4ef;
  }
  .poster-photo {
    position: absolute; inset: 0;
    background:
      radial-gradient(ellipse 260px 420px at 560px 620px, rgba(255,255,255,0.95), rgba(255,255,255,0) 70%),
      radial-gradient(ellipse 170px 220px at 560px 300px, rgba(205,140,85,0.55), rgba(205,140,85,0) 70%),
      radial-gradient(ellipse 120px 90px at 450px 540px, rgba(240,110,50,0.55), rgba(240,110,50,0) 70%),
      linear-gradient(90deg, #f7f6f2 0%, #f1eee6 45%, #e9e2d6 75%, #ddd6c8 100%);
  }
  .title { position: absolute; left: 58px; top: 58px; line-height: 0.92; font-weight: 700; font-size: 66px; letter-spacing: 1px; }
  .title-main { color: var(--blue); display: block; }
  .title-sub { color: var(--teal); display: block; }
  .subtitle-band { position: absolute; left: 0; top: 188px; width: 460px; height: 46px; }
  .subtitle-text {
    position: absolute; left: 52px; top: 199px;
    color: var(--white); font-style: italic; font-weight: 600;
    font-size: 18px; letter-spacing: 2.5px;
  }
  .promo-lead { position: absolute; left: 78px; top: 296px; font-size: 25px; font-weight: 500; line-height: 1.2; }
  .promo-value { position: absolute; left: 84px; top: 366px; font-size: 100px; font-weight: 500; color: var(--orange); line-height: 1; }
  .promo-rule { position: absolute; left: 86px; width: 256px; height: 1.5px; background: var(--ink); }
  .promo-rule.top { top: 482px; }
  .promo-rule.bottom { top: 522px; }
  .promo-note { position: absolute; left: 88px; top: 487px; font-size: 24px; font-weight: 500; }
  .event-date { position: absolute; left: 100px; top: 590px; width: 240px; height: 60px; }
  .event-day { font-size: 54px; font-weight: 600; line-height: 1; position: absolute; left: 0; top: 8px; }
  .event-suffix { font-size: 32px; font-weight: 500; line-height: 1; position: absolute; left: 64px; top: 4px; }
  .event-year { font-size: 34px; font-weight: 600; line-height: 1; position: absolute; left: 136px; top: -10px; }
  .event-month { font-size: 26px; font-weight: 500; line-height: 1; position: absolute; left: 64px; top: 36px; letter-spacing: 0.3px; }
  .event-rule { position: absolute; left: 100px; width: 240px; height: 1.5px; background: var(--ink); }
  .event-rule.top { top: 662px; }
  .event-rule.bottom { top: 726px; }
  .event-city { position: absolute; left: 102px; top: 668px; font-size: 42px; font-weight: 600; color: var(--navy); letter-spacing: 1px; }
  .brand-band { position: absolute; left: 50px; top: 812px; width: 370px; height: 104px; }
  .brand { position: absolute; left: 72px; top: 848px; display: flex; align-items: center; gap: 14px; }
  .brand-dot { width: 26px; height: 26px; border-radius: 50%; background: var(--white); }
  .brand-name { color: var(--white); font-size: 24px; font-weight: 500; }
  .brand-tagline { position: absolute; left: 404px; top: 882px; font-size: 12px; font-weight: 700; letter-spacing: 2.5px; color: var(--olive); }
  .info-lead { position: absolute; left: 212px; top: 945px; font-size: 17px; font-weight: 500; letter-spacing: 0.5px; }
  .info-band { position: absolute; left: 0; top: 940px; width: 778px; height: 110px; }
  .info-url { position: absolute; left: 0; width: 778px; top: 1000px; text-align: center; color: var(--white); font-size: 17px; font-weight: 500; letter-spacing: 4px; }
  .base-strip { position: absolute; left: 0; bottom: 0; width: 778px; height: 50px; background: linear-gradient(90deg, #eef0e6, #f3f2ec); }
</style>
</head>
<body>
  <main class="poster">
    <div class="poster-photo" role="img" aria-label="Photograph of a smiling pregnant woman in a white top holding a glass bowl of fresh salad in a bright kitchen"></div>

    <h1 class="title">
      <span class="title-main">PREGNANT</span>
      <span class="title-sub">CLASS</span>
    </h1>

    <svg class="subtitle-band" viewBox="0 0 460 46" aria-hidden="true">
      <polygon points="0,0 460,0 448,46 0,46" fill="var(--olive)"/>
    </svg>
    <p class="subtitle-text">Eating Healthy While Pregnant</p>

    <p class="promo-lead">Promote when join<br>in out class:</p>
    <p class="promo-value">30%</p>
    <div class="promo-rule top"></div>
    <p class="promo-note">off delivery package</p>
    <div class="promo-rule bottom"></div>

    <div class="event-date">
      <span class="event-day">25</span>
      <span class="event-suffix">th</span>
      <span class="event-year">2018</span>
      <span class="event-month">NOVEMBER</span>
    </div>
    <div class="event-rule top"></div>
    <p class="event-city">SINGAPORE</p>
    <div class="event-rule bottom"></div>

    <div class="base-strip"></div>

    <svg class="brand-band" viewBox="0 0 370 104" aria-hidden="true">
      <polygon points="0,0 370,0 300,104 0,104" fill="var(--olive)"/>
    </svg>
    <div class="brand">
      <span class="brand-dot"></span>
      <span class="brand-name">Harbourvale</span>
    </div>
    <p class="brand-tagline">CARE FOR EVERY STEP.</p>

    <svg class="info-band" viewBox="0 0 778 110" aria-hidden="true">
      <polygon points="0,42 190,42 190,28 778,28 778,92 0,92" fill="var(--navy)"/>
    </svg>
    <p class="info-lead">GET&nbsp; MORE INFORMATION FOR THIS POSTER.</p>
    <p class="info-url">visit at: www.harbourvalehospital.com.sg</p>
  </main>
</body>
</html>
```